Fitness Facility needs a Flyer!

We need a flyer that highlights our 3 different fitness programs.
During the sales process, we'd like to have a visual reference for new prospective clients that highlights our 3 different fitness programs.
The flyer should be colorful, Focus on the different fitness programs BUT! We'd like to steer people towards our middle program, so I'd like the middle program "The Complete Sleek & Sculpted Makeover" to be possibly a little larger than the two others so that the eye naturally gravitates towards that one.
I'd like the flyer to be in a Landscape layout,
Include our logo
Include a group photo of our team
Include the text "Most Popular" over the middle program
Include the text "Save More - 10% discount if paid in full" at the very bottom of the page
I have attached the text of our programs, a group photo, our logo and an example of our last program ... just as an example and not to be duplicated.

```html
<!DOCTYPE html>
<html lang="en">
<head>
<meta charset="utf-8">
<title>PulseForge Programs Flyer</title>
<link href="https://fonts.googleapis.com/css2?family=Montserrat:ital,wght@0,800;0,900;1,800;1,900&family=Jost:wght@300;400;500&display=swap" rel="stylesheet">
<style>
  :root{
    --maroon:#8a0a40;
    --ink:#121419;
    --yellow:#f4e100;
    --red:#c02634;
    --white:#ffffff;
    --badge-a:#ee3a2a;
    --badge-b:#8c1f8f;
  }
  *{margin:0;padding:0;box-sizing:border-box}
  html,body{width:1200px;height:848px;overflow:hidden;background:var(--maroon)}
  .flyer{position:relative;width:1200px;height:848px;overflow:hidden;font-family:"Jost",sans-serif;color:var(--white)}
  .backdrop{position:absolute;inset:0}
  .brand{position:absolute;left:920px;top:146px;width:245px;text-align:right;color:var(--ink)}
  .brand-name{font-family:"Montserrat",sans-serif;font-weight:900;font-size:44px;letter-spacing:-1px;line-height:1}
  .brand-tag{font-family:"Jost",sans-serif;font-weight:400;font-size:12px;letter-spacing:3.6px;margin-top:8px;margin-right:14px}
  .disclaimer{position:absolute;right:35px;top:227px;width:320px;text-align:right;color:var(--ink);font-size:10.3px;line-height:14.2px;font-weight:400}
  .program{position:absolute}
  .program-box{background:var(--ink)}
  .program h2{font-family:"Montserrat",sans-serif;font-weight:900;font-size:20px;letter-spacing:.4px;line-height:1;text-transform:uppercase}
  .program ul{list-style:none}
  .program li{font-size:12px;font-weight:400;line-height:14.2px}
  .lean-prep{left:33px;top:475px;width:251px;height:286px;padding:28px 0 0 29px}
  .lean-prep ul{margin-top:22px}
  .lean-prep li{margin-bottom:14.3px}
  .makeover{left:325px;top:418px;width:470px;height:382px}
  .makeover h2{position:absolute;left:20px;top:9px;font-size:21px;line-height:20px;width:330px}
  .makeover ul{position:absolute;left:20px;top:76px;width:340px}
  .makeover li{margin-bottom:14.3px;font-size:12.4px}
  .makeover-frame{position:absolute;inset:0;overflow:visible}
  .blitz{left:826px;top:318px;width:298px;height:370px;padding:26px 0 0 24px}
  .blitz h2{font-size:19px}
  .blitz ul{margin-top:20px}
  .blitz li{margin-bottom:14.3px;font-size:11px;font-weight:500}
  .price{position:absolute;width:90px;height:90px;border-radius:50%;border:3px solid var(--yellow);background:linear-gradient(35deg,var(--badge-a) 20%,var(--badge-b) 85%);text-align:center;font-family:"Montserrat",sans-serif;color:var(--white)}
  .price .only{display:block;font-weight:900;font-style:italic;font-size:14px;line-height:1;margin-top:10px}
  .price .amount{display:block;font-weight:900;font-size:33px;line-height:1;letter-spacing:-1px}
  .price .per{display:block;font-weight:800;font-style:italic;font-size:10px;line-height:1}
  .price-47{left:95px;top:704px}
  .price-47 .amount{margin-top:22px}
  .price-69{left:668px;top:704px}
  .price-125{left:934px;top:628px}
  .price-125 .amount{margin-top:21px;font-size:29px}
  .stamp{position:absolute;left:705px;top:436px;width:96px;height:96px;border-radius:50%;border:3px solid var(--white);display:flex;align-items:center;justify-content:center;transform:rotate(-18deg)}
  .stamp::before{content:"";position:absolute;inset:5px;border-radius:50%;border:1.5px solid var(--white)}
  .stamp span{font-family:"Montserrat",sans-serif;font-weight:900;font-size:16px;line-height:15px;text-align:center;text-transform:uppercase}
  .save-more{position:absolute;left:836px;top:752px;font-size:17px;font-weight:300;letter-spacing:.2px}
</style>
</head>
<body>
<div class="flyer">
  <svg class="backdrop" width="1200" height="848" viewBox="0 0 1200 848">
    <defs>
      <linearGradient id="photoTone" x1="0" y1="0" x2="1" y2="1">
        <stop offset="0" stop-color="#3d4f6e"/>
        <stop offset=".45" stop-color="#6a4a5c"/>
        <stop offset=".8" stop-color="#2a2a33"/>
      </linearGradient>
    </defs>
    <rect width="1200" height="848" fill="var(--maroon)"/>
    <circle cx="1111" cy="235" r="300" fill="var(--red)"/>
    <g role="img" aria-label="Group photo of the training team and members cheering together in the gym">
      <polygon points="0,0 1200,0 1200,370 0,430" fill="url(#photoTone)"/>
    </g>
    <polygon points="0,426 1200,366 1200,373 0,434" fill="var(--yellow)"/>
    <circle cx="1111" cy="235" r="254" fill="var(--ink)"/>
    <circle cx="1111" cy="235" r="245" fill="var(--yellow)"/>
  </svg>

  <div class="brand">
    <div class="brand-name">PulseForge</div>
    <div class="brand-tag">Personal Group Training</div>
  </div>
  <p class="disclaimer">Disclaimer –<br>We are not a Boot Camp with “fitness classes”<br>We are professional training facility with Full Fitness<br>Programs that Deliver Results!</p>

  <section class="program program-box lean-prep">
    <h2>Lean Body Prep</h2>
    <ul>
      <li>4 Group Training Sessions per week</li>
      <li>Customized Meal Plan</li>
      <li>Monthly BodyComp Scans</li>
      <li>Supplement List</li>
      <li>Access to Private PulseForge<br>Circle Group</li>
    </ul>
  </section>
  <div class="price price-47"><span class="amount">$47</span><span class="per">PER WEEK</span></div>

  <section class="program makeover">
    <svg class="makeover-frame" width="470" height="382" viewBox="0 0 470 382">
      <polyline points="371,57 0,57 0,382 348,382" fill="none" stroke="var(--yellow)" stroke-width="1.5"/>
      <line x1="465" y1="108" x2="465" y2="382" stroke="var(--yellow)" stroke-width="1.5"/>
    </svg>
    <h2>The Complete Sleek &amp;<br>Sculpted Makeover</h2>
    <ul>
      <li>UNLIMITED Group Training Sessions Designed to Sculpt &amp; Tone the body</li>
      <li>Customized AND Phased Nutrition Plans so your metabolism never plateaus</li>
      <li>Your own Accountability Coach who will be your biggest cheerleader and motivator</li>
      <li>Weekly accountability Check In’s</li>
      <li>Bi-weekly 1-on-1 accountability &amp; strategy meetups</li>
      <li>Bi-weekly BodyComp Scans</li>
      <li>Supplement List to accelerate metabolism</li>
      <li>Exclusive access to PulseForge’s Private<br>Circle Page for additional Recipes,<br>Support and Guidance</li>
    </ul>
  </section>
  <div class="stamp"><span>Most<br>Popular</span></div>
  <div class="price price-69"><span class="only">ONLY</span><span class="amount">$69</span><span class="per">PER WEEK</span></div>

  <section class="program program-box blitz">
    <h2>1-on-1 Fitness Blitz</h2>
    <ul>
      <li>(8) 1-on-1 Personal Training Sessions per month</li>
      <li>UNLIMITED Group Training Sessions</li>
      <li>Customized AND Phased Nutrition Plans</li>
      <li>Designated Accountability Coach</li>
      <li>Weekly accountability check in’s</li>
      <li>Weekly BodyComp Scans</li>
      <li>Exclusive Supplement Discounts</li>
      <li>Exclusive access to PulseForge’s Circle Page</li>
    </ul>
  </section>
  <div class="price price-125"><span class="amount">$125</span><span class="per">PER WEEK</span></div>

  <p class="save-more">SAVE MORE - 10% discount if paid in full</p>
</div>
</body>
</html>
```